Edutainment company need help with Squarespace design

Need help completing website design for a hybrid education and entertainment company called "Novaflickerium". The website will be based through Squarespace. A lot has been done, but need help to make look more consistent with branding and dynamic. Attached is brand kit already created by wonderful designer. Just want help keeping a professional look.

```html
<!DOCTYPE html>
<html lang="en">
<head>
<meta charset="utf-8">
<title>Novaflickerium</title>
<link href="https://fonts.googleapis.com/css2?family=Luckiest+Guy&family=Roboto:ital,wght@0,400;0,500;1,400&display=swap" rel="stylesheet">
<style>
:root{
  --purple:#6a3f9c;
  --purple-dark:#5b3496;
  --yellow:#fcc23d;
  --cream:#fbf4ee;
  --sand:#f2e9e2;
  --ink:#2b2b2b;
  --muted:#555;
  --white:#fff;
}
*{margin:0;padding:0;box-sizing:border-box}
html,body{width:1200px;height:4677px;overflow:hidden}
body{position:relative;background:var(--white);font-family:"Roboto",Arial,sans-serif;color:var(--ink)}
.display{font-family:"Luckiest Guy","Arial Black",sans-serif;font-weight:400;letter-spacing:1px}
.abs{position:absolute}

/* header */
.site-header{position:absolute;left:0;top:0;width:1200px;height:160px;background:var(--purple)}
.brand{position:absolute;display:flex;align-items:center;gap:12px;font-family:"Luckiest Guy",sans-serif;color:var(--white)}
.brand-dot{border-radius:50%;background:var(--yellow)}
.header-brand{left:127px;top:58px;font-size:32px}
.header-brand .brand-dot{width:22px;height:22px}
.call{position:absolute;right:128px;top:40px;font-family:"Luckiest Guy",sans-serif;font-size:28px;color:var(--white);display:flex;align-items:center;gap:10px}
.call .label{color:var(--yellow)}
.main-nav{position:absolute;right:128px;top:104px;display:flex;gap:40px;font-family:"Luckiest Guy",sans-serif;font-size:22px;color:var(--white)}
.main-nav .active{color:var(--yellow)}

/* hero */
.hero{position:absolute;left:0;top:160px;width:1200px;height:566px;background:linear-gradient(90deg,#e5d3bd 0%,#e8d8c4 45%,#cdb59a 70%,#8a5a34 100%)}
.hero-photo{position:absolute;right:0;top:0;width:560px;height:566px;background:radial-gradient(circle at 62% 40%,#c06a2a 0%,#a55a26 22%,#c9a98a 48%,rgba(205,181,154,0) 75%)}
.hero-title{position:absolute;left:127px;top:146px;font-size:50px;line-height:48px;color:var(--purple-dark)}
.hero-text{position:absolute;left:127px;top:265px;width:460px;font-size:19px;line-height:23px;color:#222}
.btn{display:inline-flex;align-items:center;justify-content:center;font-family:"Luckiest Guy",sans-serif;color:var(--white);background:var(--purple);border-radius:8px}
.hero .btn{position:absolute;left:127px;top:352px;width:196px;height:65px;font-size:22px}

/* section headings */
.section-title{position:absolute;left:0;width:1200px;text-align:center;color:var(--purple-dark);font-size:48px}
.title-bar{position:absolute;left:561px;top:816px;width:78px;height:6px;background:var(--yellow)}

/* what we do */
.service{position:absolute;width:330px;text-align:center}
.service .photo{width:270px;height:270px;border-radius:50%;margin:0 auto}
.service h3{margin-top:26px;font-family:"Luckiest Guy",sans-serif;font-weight:400;font-size:30px;color:var(--purple-dark)}
.service p{margin-top:12px;font-size:14.5px;line-height:22px;color:#333}

/* why */
.why{position:absolute;left:0;top:1447px;width:1200px;height:606px;background:var(--cream)}
.feature{position:absolute;width:470px}
.feature .icon{position:absolute;left:0;top:0;width:145px;height:145px;border-radius:50%;background:var(--purple);display:flex;align-items:center;justify-content:center}
.feature h4{position:absolute;left:163px;top:12px;font-family:"Luckiest Guy",sans-serif;font-weight:400;font-size:21px;line-height:24px;color:var(--purple-dark)}
.feature p{position:absolute;left:163px;top:68px;width:290px;font-size:14.5px;line-height:18px;color:#333}

/* classes */
.class-card{position:absolute;top:2233px;width:298px;height:439px;border:1px solid #ddd;border-radius:6px;background:var(--white);overflow:hidden;box-shadow:0 2px 6px rgba(0,0,0,.05)}
.class-card .photo{height:223px}
.class-card .tag{position:absolute;left:24px;top:254px;font-family:"Luckiest Guy",sans-serif;font-size:18px;color:var(--yellow)}
.class-card h3{position:absolute;left:24px;top:278px;font-family:"Luckiest Guy",sans-serif;font-weight:400;font-size:22px;line-height:25px;color:var(--purple-dark)}
.class-card p{position:absolute;left:24px;top:352px;width:250px;font-size:14px;line-height:22px;color:var(--muted)}
.pager{position:absolute;top:2744px;left:450px;display:flex;gap:18px}
.pager span{width:62px;height:3px;background:#ddd}
.pager .on{background:var(--yellow)}

/* testimonial */
.testimonial{position:absolute;left:0;top:2824px;width:1200px;height:499px;background:var(--sand)}
.student-photo{position:absolute;left:169px;top:116px;width:281px;height:281px;border-radius:50%;background:radial-gradient(circle at 50% 40%,#9b6a4e 0%,#4a5f86 45%,#d8a35c 80%)}
.quote-text{position:absolute;left:510px;top:170px;width:560px;font-size:25px;line-height:32px;font-style:italic;color:#222}
.quote-name{position:absolute;left:510px;top:338px;font-family:"Luckiest Guy",sans-serif;font-size:21px;color:var(--purple-dark)}
.quote-role{position:absolute;left:510px;top:368px;font-size:14px;font-weight:500;color:#222}
.decor{position:absolute;right:60px;bottom:0;width:290px;height:140px;border-radius:150px 150px 0 0;background:rgba(106,63,156,.05)}

/* articles */
.article{position:absolute;top:3512px;width:298px;text-align:center}
.article .photo{height:332px;border-radius:4px}
.article h3{margin-top:32px;font-family:"Luckiest Guy",sans-serif;font-weight:400;font-size:20px;line-height:25px;color:var(--purple-dark)}
.article time{display:block;margin-top:10px;font-size:14px;font-weight:500;color:#222}

/* newsletter */
.newsletter{position:absolute;left:0;top:4048px;width:1200px;height:268px;background:var(--yellow)}
.newsletter h2{position:absolute;left:183px;top:68px;font-family:"Luckiest Guy",sans-serif;font-weight:400;font-size:40px;color:var(--purple-dark)}
.newsletter p{position:absolute;left:183px;top:120px;font-size:19px;color:#222}
.signup{position:absolute;left:183px;top:163px;width:517px;height:54px;border:2px solid var(--purple-dark);border-radius:8px;background:var(--yellow)}
.signup .field{position:absolute;left:16px;top:15px;font-size:18px;color:#222}
.signup .btn{position:absolute;right:4px;top:4px;width:121px;height:42px;font-size:19px;background:var(--purple-dark)}

/* footer */
.site-footer{position:absolute;left:0;top:4316px;width:1200px;height:361px;background:var(--purple)}
.footer-brand{left:131px;top:126px;font-size:34px}
.footer-brand .brand-dot{width:26px;height:26px}
.vline{position:absolute;top:49px;width:2px;height:227px;background:rgba(255,255,255,.35)}
.vline::before{content:"";position:absolute;left:-1px;top:0;width:4px;height:22px;background:var(--yellow);border-radius:2px}
.footer-col h5{position:absolute;top:56px;font-family:"Luckiest Guy",sans-serif;font-weight:400;font-size:22px;color:var(--white)}
.footer-links{position:absolute;left:595px;top:96px;list-style:none;font-size:14px;line-height:26px;color:var(--white)}
.contact-list{position:absolute;left:868px;top:96px;list-style:none;font-size:14px;line-height:18px;color:var(--white);width:210px}
.contact-list li{display:flex;gap:10px;margin-bottom:18px}
.contact-list svg{flex:none;margin-top:2px}
.hline{position:absolute;left:127px;top:284px;width:944px;height:1px;background:rgba(255,255,255,.35)}
.social{position:absolute;left:127px;top:316px;display:flex;gap:16px}
.social span{width:22px;height:22px;border-radius:50%;background:var(--white)}
.copyright{position:absolute;right:129px;top:319px;font-size:14px;color:var(--white)}
</style>
</head>
<body>

<header class="site-header">
  <div class="brand header-brand"><span class="brand-dot"></span>Novaflickerium</div>
  <div class="call">
    <svg width="26" height="26" viewBox="0 0 24 24" fill="#fcc23d"><path d="M6.6 10.8a15 15 0 0 0 6.6 6.6l2.2-2.2a1 1 0 0 1 1-.25 11.4 11.4 0 0 0 3.6.57 1 1 0 0 1 1 1V20a1 1 0 0 1-1 1A17 17 0 0 1 3 4a1 1 0 0 1 1-1h3.5a1 1 0 0 1 1 1c0 1.25.2 2.45.57 3.57a1 1 0 0 1-.25 1z"/></svg>
    <span class="label">Call:</span> +123 456 7890
  </div>
  <nav class="main-nav"><span class="active">Home</span><span>About</span><span>What We Do</span><span>Why Us?</span><span>Contact</span></nav>
</header>

<section class="hero">
  <div class="hero-photo" role="img" aria-label="Smiling woman with glasses holding a mug at a desk with a laptop"></div>
  <h1 class="hero-title display">Welcome to<br>Novaflickerium</h1>
  <p class="hero-text">Lorem ipsum dolor sit amet, consectetur adipiscing elit, sed do eiusmod tempor incididunt ut labore et dolore magna aliqua.</p>
  <a class="btn">Get Started</a>
</section>

<div class="title-bar"></div>
<h2 class="section-title display" style="top:832px">What We Do</h2>
<div class="service" style="left:104px;top:931px">
  <div class="photo" role="img" aria-label="Music teacher conducting a class" style="background:radial-gradient(circle at 50% 45%,#a8345a 0%,#7a4a3a 40%,#c8a57a 80%)"></div>
  <h3>Title Here</h3>
  <p>Lorem ipsum dolor sit amet, consectetur adipiscingelit orem ipsum dolor sit amet consectetur adipiscing elid ut picia.</p>
</div>
<div class="service" style="left:434px;top:931px">
  <div class="photo" role="img" aria-label="Student with headphones studying on a laptop in a library" style="background:radial-gradient(circle at 50% 50%,#c9a88a 0%,#6e4a35 50%,#3d2a20 90%)"></div>
  <h3>Title Here</h3>
  <p>Lorem ipsum dolor sit amet, consectetur adipiscingelit orem ipsum dolor sit amet consectetur adipiscing elid ut picia.</p>
</div>
<div class="service" style="left:764px;top:931px">
  <div class="photo" role="img" aria-label="Woman taking notes beside a laptop" style="background:radial-gradient(circle at 50% 45%,#8a7a6a 0%,#cfc8bd 50%,#e8e6e0 85%)"></div>
  <h3>Title Here</h3>
  <p>Lorem ipsum dolor sit amet, consectetur adipiscingelit orem ipsum dolor sit amet consectetur adipiscing elid ut picia.</p>
</div>

<section class="why">
  <h2 class="section-title display" style="top:70px">Why Choose Us?</h2>
  <div class="feature" style="left:127px;top:201px">
    <div class="icon"><svg width="70" height="70" viewBox="0 0 64 64" fill="none" stroke="#fcc23d" stroke-width="3"><circle cx="28" cy="30" r="20"/><path d="M28 18v12l8 6"/><circle cx="44" cy="44" r="11" fill="#6a3f9c"/><path d="M44 38v12M41 41h5a2 2 0 0 1 0 4h-4a2 2 0 0 0 0 4h5"/></svg></div>
    <h4>Flexibility<br>and Accessibility</h4>
    <p>Lorem ipsum dolor sit amet, consectetur adipiscing elit orem ipsum dolor sit amet consectetur adipiscing elit.</p>
  </div>
  <div class="feature" style="left:632px;top:201px">
    <div class="icon"><svg width="72" height="72" viewBox="0 0 64 64" fill="none" stroke="#fcc23d" stroke-width="3"><path d="M8 16h18a6 6 0 0 1 6 6v28a5 5 0 0 0-5-5H8zM56 16H38a6 6 0 0 0-6 6v28a5 5 0 0 1 5-5h19z"/><path d="M13 24h12M13 31h12M39 24h12M39 31h12"/></svg></div>
    <h4>Personalised<br>Learning Paths</h4>
    <p>Lorem ipsum dolor sit amet, consectetur adipiscing elit orem ipsum dolor sit amet consectetur adipiscing elit.</p>
  </div>
  <div class="feature" style="left:127px;top:386px">
    <div class="icon"><svg width="72" height="72" viewBox="0 0 64 64" fill="none" stroke="#fcc23d" stroke-width="3"><path d="M8 54h48"/><rect x="12" y="40" width="8" height="14"/><rect x="26" y="32" width="8" height="22"/><rect x="40" y="24" width="8" height="30"/><path d="M12 30l14-10 8 6 16-16M42 10h8v8"/></svg></div>
    <h4>Increased Student<br>Engagement</h4>
    <p>Lorem ipsum dolor sit amet, consectetur adipiscing elit orem ipsum dolor sit amet consectetur adipiscing elit.</p>
  </div>
  <div class="feature" style="left:632px;top:386px">
    <div class="icon"><svg width="72" height="72" viewBox="0 0 64 64" fill="none" stroke="#fcc23d" stroke-width="3"><circle cx="32" cy="14" r="8"/><path d="M14 36l18-8 18 8v16l-18 8-18-8z"/><path d="M14 36l18 8 18-8M32 44v16"/></svg></div>
    <h4>Improved<br>Learning Outcomes</h4>
    <p>Lorem ipsum dolor sit amet, consectetur adipiscing elit orem ipsum dolor sit amet consectetur adipiscing elit.</p>
  </div>
</section>

<h2 class="section-title display" style="top:2118px">Our Classes</h2>
<article class="class-card" style="left:112px">
  <div class="photo" role="img" aria-label="Students at a piano lesson" style="background:linear-gradient(135deg,#6b5140,#e0a040 50%,#3a4f78)"></div>
  <span class="tag">In Person</span>
  <h3>Lorem ipsum dolor<br>sit amet, consectet</h3>
  <p>Lorem ipsum dolor sit amet, cons ectetur adipiscing elit, sed loredo eiusmod tempor incididunt.</p>
</article>
<article class="class-card" style="left:450px">
  <div class="photo" role="img" aria-label="Person typing on a laptop" style="background:linear-gradient(135deg,#d8c2a8,#c9a688 50%,#e6e2dc)"></div>
  <span class="tag">Online</span>
  <h3>Lorem ipsum dolor<br>sit amet, consectet</h3>
  <p>Lorem ipsum dolor sit amet, cons ectetur adipiscing elit, sed loredo eiusmod tempor incididunt.</p>
</article>
<article class="class-card" style="left:790px">
  <div class="photo" role="img" aria-label="Smiling woman in an olive shirt" style="background:linear-gradient(135deg,#3a3a3a,#c09a70 45%,#7a7a55)"></div>
  <span class="tag">Online</span>
  <h3>Lorem ipsum dolor<br>sit amet, consectet</h3>
  <p>Lorem ipsum dolor sit amet, cons ectetur adipiscing elit, sed loredo eiusmod tempor incididunt.</p>
</article>
<div class="pager"><span class="on"></span><span></span><span></span><span></span></div>

<section class="testimonial">
  <div class="student-photo" role="img" aria-label="Smiling student with glasses and headphones"></div>
  <svg class="abs" style="left:501px;top:73px" width="98" height="72" viewBox="0 0 98 72" fill="#fcc23d"><path d="M24 0a24 24 0 0 1 20 36c-6 12-18 26-30 36 6-10 10-20 8-26A24 24 0 0 1 24 0zM74 0a24 24 0 0 1 20 36c-6 12-18 26-30 36 6-10 10-20 8-26A24 24 0 0 1 74 0z"/></svg>
  <p class="quote-text">Lorem ipsum dolor sit amet, consectetur adipisci elit, sed do eiusmod tempor incididunt ut laboreet dolore magna aliqua. Quis ipsum suspendi sse ultrices gravidsus commodo viverra</p>
  <div class="quote-name">-Jesika Lorem</div>
  <div class="quote-role">STYDENT NAME</div>
  <div class="decor" role="img" aria-label="Faint doodle decoration"></div>
</section>

<h2 class="section-title display" style="top:3398px">Latest Articles</h2>
<article class="article" style="left:112px">
  <div class="photo" role="img" aria-label="Students at a piano lesson" style="background:linear-gradient(180deg,#6b5140,#d09a40 45%,#5b3496)"></div>
  <h3>Lorem ipsum dolor sit<br>amet, consectet ur</h3>
  <time>AUG 19 2025</time>
</article>
<article class="article" style="left:450px">
  <div class="photo" role="img" aria-label="Person typing on a laptop" style="background:linear-gradient(180deg,#e0cdb6,#c9a688 50%,#5b3496)"></div>
  <h3>Lorem ipsum dolor sit<br>amet, consectet ur</h3>
  <time>AUG 19 2025</time>
</article>
<article class="article" style="left:790px">
  <div class="photo" role="img" aria-label="Smiling woman in an olive shirt" style="background:linear-gradient(180deg,#3a3a3a,#b89870 40%,#5b3496)"></div>
  <h3>Lorem ipsum dolor sit<br>amet, consectet ur</h3>
  <time>AUG 19 2025</time>
</article>

<section class="newsletter">
  <h2>Subscribe to Newsletter</h2>
  <p>Lorem ipsum dolor sit ame onsectetur adipiscin.</p>
  <div class="signup"><span class="field">Email:</span><a class="btn">Sign Up</a></div>
  <div class="abs" role="img" aria-label="Faint doodle decoration" style="right:0;top:60px;width:260px;height:208px;border-radius:130px 0 0 0;background:rgba(255,255,255,.12)"></div>
</section>

<footer class="site-footer">
  <div class="brand footer-brand"><span class="brand-dot"></span>Novaflickerium</div>
  <div class="vline" style="left:508px"></div>
  <div class="vline" style="left:770px"></div>
  <div class="footer-col"><h5 style="left:595px">Links</h5></div>
  <ul class="footer-links"><li>Home</li><li>About</li><li>What We Do</li><li>Meet the team</li><li>Contact us</li><li>Blog</li></ul>
  <div class="footer-col"><h5 style="left:868px">Contact</h5></div>
  <ul class="contact-list">
    <li><svg width="12" height="14" viewBox="0 0 12 16" fill="#fff"><path d="M6 0a6 6 0 0 1 6 6c0 4.5-6 10-6 10S0 10.5 0 6a6 6 0 0 1 6-6zm0 4a2 2 0 1 0 0 4 2 2 0 0 0 0-4z"/></svg><span>Lorem Dum street 123 LJD dumy numers 463.</span></li>
    <li><svg width="13" height="13" viewBox="0 0 24 24" fill="#fff"><path d="M6.6 10.8a15 15 0 0 0 6.6 6.6l2.2-2.2a1 1 0 0 1 1-.25 11.4 11.4 0 0 0 3.6.57 1 1 0 0 1 1 1V20a1 1 0 0 1-1 1A17 17 0 0 1 3 4a1 1 0 0 1 1-1h3.5a1 1 0 0 1 1 1c0 1.25.2 2.45.57 3.57a1 1 0 0 1-.25 1z"/></svg><span>Phone: 23 456 7890</span></li>
    <li><svg width="14" height="12" viewBox="0 0 16 12" fill="#fff"><path d="M0 0h16v12H0zM1 1l7 5 7-5"/><path d="M1 1l7 5 7-5" stroke="#6a3f9c" stroke-width="1.5" fill="none"/></svg><span>Email:info@company.com</span></li>
  </ul>
  <div class="hline"></div>
  <div class="social"><span></span><span></span><span></span><span></span></div>
  <div class="copyright">Copyright © 2025 Novaflickerium. All Rights Reserved.</div>
</footer>

</body>
</html>
```